Brightpath Dentistry - Flyer - Modern & Eye catching campaign flyer

Need front & back side full page flyer designs for both 1) Grand opening 2) On-going campaign.

Attached the new dental office logo.
Attached our other dental clinic flyer designs for content.

Target Market(s)

Cosmetic dentistry

Industry/Entity Type

Health Care

Requirements
Must have
• decent, modern and eye catching marketing flyers.
Nice to have
• - Nice space
• - Highlight phone number
• - Highlight special features like convenient hours, call or text, for all ages, digital facility, etc
Should not have
• - Don't want to fill the flyer with too much wordings
• - Too many colors

```html
<!DOCTYPE html>
<html lang="en">
<head>
<meta charset="utf-8">
<title>Brightpath Dentistry Flyer</title>
<link rel="stylesheet" href="https://fonts.googleapis.com/css2?family=Open+Sans:wght@400;600;700;800&family=Barlow+Condensed:ital,wght@0,600;0,700;1,700&display=swap">
<style>
  :root{
    --blue:#3158a9;
    --navy:#1f2f6e;
    --sky:#4f9ad3;
    --sky-soft:#9fd0ee;
    --green:#4f8f2a;
    --ink:#2a2a2a;
    --paper:#ffffff;
    --stage:#eef1f5;
  }
  *{margin:0;padding:0;box-sizing:border-box}
  html,body{width:1200px;height:1200px;overflow:hidden;background:var(--stage)}
  body{font-family:"Open Sans",sans-serif;color:var(--ink)}
  .flyer{position:absolute;left:185px;top:27px;width:830px;height:1146px;background:var(--paper);overflow:hidden;box-shadow:0 4px 18px rgba(0,0,0,.12)}
  .flyer-art{position:absolute;inset:0}
  .abs{position:absolute}

  .experience-tag{left:14px;top:0;width:194px;height:184px;background:linear-gradient(160deg,#4b73c0,#24478f);color:#fff}
  .experience-tag p{position:absolute;left:26px;top:46px;transform:rotate(9deg);transform-origin:left top;line-height:1.05}
  .experience-tag .years{font-size:36px;font-weight:400;display:block}
  .experience-tag .label{font-size:26px;font-weight:400;display:block;margin-left:-12px}

  .brand{left:330px;top:40px;display:flex;align-items:center;gap:16px}
  .brand-dot{width:64px;height:64px;border-radius:50%;background:var(--sky)}
  .brand-name{font-weight:700;color:var(--sky);font-size:44px;letter-spacing:1px;line-height:1}

  .headline{left:432px;top:362px;font-family:"Barlow Condensed",sans-serif;font-style:italic;font-weight:700;font-size:43px;line-height:1.17;color:var(--ink)}
  .headline .accent{color:var(--sky)}

  .badge-text{left:539px;top:604px;width:180px;text-align:center;font-family:"Barlow Condensed",sans-serif;font-weight:700;line-height:1}
  .badge-text .all{font-size:44px;color:var(--green);display:block}
  .badge-text .ins{font-size:35px;color:var(--blue);display:block;margin-top:4px;letter-spacing:-.5px}
  .badge-text .acc{font-size:32px;color:var(--green);display:block;margin-top:6px}

  .services-title{left:24px;top:961px;transform:rotate(-90deg);transform-origin:left top;font-size:46px;font-weight:800;color:var(--navy);white-space:nowrap;letter-spacing:-.5px}
  .service{width:180px;text-align:center;font-size:15px;font-weight:700;color:var(--navy);line-height:1.25;text-transform:uppercase}
  .service svg{display:block;margin:0 auto 6px}
  .service .note{text-transform:none}
  .col-rule{left:224px;top:558px;width:3px;height:478px;background:var(--blue)}

  .contact{left:475px;top:793px;width:300px;text-align:center}
  .contact .lead{font-size:19px;color:var(--sky);font-weight:400}
  .contact .phone{display:flex;align-items:center;justify-content:center;gap:6px;font-size:31px;color:var(--ink);margin-top:6px}

  .map{left:475px;top:872px;width:300px;height:186px;border-radius:22px;background:var(--sky-soft);padding:12px}
  .map-area{width:100%;height:100%;border-radius:14px;background:linear-gradient(135deg,#e3e5e8,#d3d7dc)}

  .welcome{left:32px;top:1060px;font-size:25px;font-weight:800;color:var(--blue);letter-spacing:-.3px;white-space:nowrap}
  .address{left:452px;top:1066px;display:flex;align-items:center;gap:6px;font-size:17px;font-weight:700;color:var(--blue);white-space:nowrap}
</style>
</head>
<body>
<main class="flyer">
  <svg class="flyer-art" width="830" height="1146" viewBox="0 0 830 1146">
    <defs>
      <linearGradient id="photoTone" x1="0" y1="0" x2="1" y2="1">
        <stop offset="0" stop-color="#d9dde6"/>
        <stop offset=".5" stop-color="#eef0f4"/>
        <stop offset="1" stop-color="#c8cfdc"/>
      </linearGradient>
      <linearGradient id="roomTone" x1="0" y1="0" x2="1" y2="1">
        <stop offset="0" stop-color="#f6f8fb"/>
        <stop offset=".6" stop-color="#eef1f7"/>
        <stop offset="1" stop-color="#f7f8fb"/>
      </linearGradient>
      <radialGradient id="badgeTone" cx=".4" cy=".35" r=".7">
        <stop offset="0" stop-color="#ffffff"/>
        <stop offset=".7" stop-color="#eceef1"/>
        <stop offset="1" stop-color="#c9cdd3"/>
      </radialGradient>
    </defs>
    <polygon points="0,470 830,669 830,1146 0,1146" fill="url(#roomTone)" role="img" aria-label="Soft background photo of a bright dental treatment room with a patient chair"/>
    <polygon points="0,62 830,288 830,669 0,470" fill="url(#photoTone)" role="img" aria-label="Photo of a smiling young patient in a dental chair with a masked dentist giving a thumbs up"/>
    <polygon points="0,55 830,281 830,295 0,69" fill="var(--blue)"/>
    <polygon points="0,462 830,661 830,677 0,478" fill="var(--blue)"/>
    <circle cx="629" cy="667" r="110" fill="url(#badgeTone)" stroke="var(--blue)" stroke-width="8"/>
  </svg>

  <div class="abs experience-tag"><p><span class="years">10 Years</span><span class="label">of Experience</span></p></div>

  <div class="abs brand"><span class="brand-dot"></span><span class="brand-name">Brightpath<br>Dentistry</span></div>

  <h1 class="abs headline">YOUR<br>DENTAL <span class="accent">HEALTH IS</span><br><span class="accent">OUR FRIST</span> PRIORITY!</h1>

  <div class="abs badge-text"><span class="all">All</span><span class="ins">INSURANCES</span><span class="acc">ACCEPTED</span></div>

  <h2 class="abs services-title">OUR SERVICES</h2>
  <div class="abs col-rule"></div>

  <div class="abs service" style="left:54px;top:557px">
    <svg width="40" height="40" viewBox="0 0 40 40"><path d="M8 8c4-5 9-2 12 0 3-2 8-5 12 0 3 5 1 12-1 16l-3 12c-1 2-3 2-4 0l-2-9c-1-2-3-2-4 0l-2 9c-1 2-3 2-4 0L9 24C7 20 5 13 8 8z" fill="none" stroke="var(--blue)" stroke-width="3"/><path d="M17 14v14M23 14v14" stroke="var(--blue)" stroke-width="2"/></svg>
    Root Canal<br>Therapy</div>
  <div class="abs service" style="left:54px;top:663px">
    <svg width="40" height="40" viewBox="0 0 40 40"><path d="M10 8c4-4 8-2 10 0 2-2 6-4 10 0 3 4 1 10-1 14l-3 12c-1 2-3 2-4 0l-2-8-2 8c-1 2-3 2-4 0l-3-12C9 18 7 12 10 8z" fill="var(--blue)"/><path d="M3 6l4 3M37 6l-4 3M2 16h4M38 16h-4" stroke="var(--blue)" stroke-width="2"/></svg>
    Glow Teeth<br>Whitening</div>
  <div class="abs service" style="left:54px;top:773px">
    <svg width="48" height="42" viewBox="0 0 48 42"><path d="M4 14q20 28 40 0v10q-20 26-40 0z" fill="var(--blue)"/><path d="M14 6c3-3 7-1 10 0 3-1 7-3 10 0 2 4 0 9-2 13l-2 6c-1 2-2 2-3 0l-3-7-3 7c-1 2-2 2-3 0l-2-6c-2-4-4-9-2-13z" fill="#fff" stroke="var(--blue)" stroke-width="2.5"/></svg>
    Extractions</div>
  <div class="abs service" style="left:54px;top:866px">
    <svg width="40" height="46" viewBox="0 0 40 46"><path d="M8 4c4-4 8-2 12 0 4-2 8-4 12 0 3 5 0 11-3 14H11C8 15 5 9 8 4z" fill="var(--blue)"/><path d="M13 22h14l-2 4H15zM14 29h12l-2 4h-8zM16 36h8l-4 8z" fill="var(--blue)"/></svg>
    Implants</div>
  <div class="abs service" style="left:54px;top:962px">
    <svg width="60" height="32" viewBox="0 0 60 32"><path d="M4 20q0-16 26-16t26 16v6H4z" fill="none" stroke="var(--blue)" stroke-width="3"/><path d="M8 22h44M16 12v10M24 9v13M32 9v13M40 9v13M48 14v8" stroke="var(--blue)" stroke-width="2.5"/></svg>
    Dentures</div>

  <div class="abs service" style="left:219px;top:620px">
    <svg width="48" height="40" viewBox="0 0 48 40"><path d="M4 10q20-10 40 0v12q-20 10-40 0z" fill="none" stroke="var(--blue)" stroke-width="3"/><path d="M12 12v10M20 10v14M28 10v14M36 12v10" stroke="var(--blue)" stroke-width="2.5"/></svg>
    Veneers</div>
  <div class="abs service" style="left:219px;top:707px">
    <svg width="66" height="28" viewBox="0 0 66 28"><path d="M4 4h58v8H4z" fill="var(--blue)"/><path d="M6 12h11l-2 14h-7zM20 12h11l-2 14h-7zM35 12h11l-2 14h-7zM49 12h11l-2 14h-7z" fill="var(--blue)"/><path d="M2 8h62" stroke="#fff" stroke-width="1.5"/></svg>
    ClearFit<br><span class="note">(Invisible braces)</span></div>
  <div class="abs service" style="left:219px;top:805px">
    <svg width="56" height="28" viewBox="0 0 56 28"><rect x="3" y="5" width="50" height="18" rx="9" fill="none" stroke="var(--blue)" stroke-width="3"/><path d="M11 9v10M19 8v12M28 8v12M37 8v12M45 9v10" stroke="var(--blue)" stroke-width="2.5"/></svg>
    Night Guards</div>
  <div class="abs service" style="left:219px;top:890px">
    <svg width="40" height="46" viewBox="0 0 40 46"><path d="M6 4h28v10H6z" fill="var(--blue)"/><path d="M8 16c4-2 8 0 12 2 4-2 8-4 12-2 2 5 0 10-2 14l-3 12c-1 2-3 2-4 0l-3-9-3 9c-1 2-3 2-4 0l-3-12c-2-4-4-9-2-14z" fill="none" stroke="var(--blue)" stroke-width="3"/></svg>
    Crown and<br>Bridge</div>

  <div class="abs contact">
    <p class="lead">CALL OR TEXT US</p>
    <p class="phone"><svg width="20" height="34" viewBox="0 0 20 34"><rect x="2" y="2" width="16" height="30" rx="3" fill="none" stroke="var(--blue)" stroke-width="3"/><path d="M7 27h6" stroke="var(--blue)" stroke-width="2"/></svg>610.555.0142</p>
  </div>

  <div class="abs map"><div class="map-area" role="img" aria-label="Street map showing the office location"></div></div>

  <p class="abs welcome">NEW PATIENTS ARE WELCOME!</p>
  <p class="abs address"><svg width="12" height="16" viewBox="0 0 12 16"><path d="M6 15C2 10 1 8 1 6a5 5 0 0 1 10 0c0 2-1 4-5 9z" fill="#c5cbd6"/><circle cx="6" cy="6" r="2" fill="#fff"/></svg>412 Harbor Pike, Maple Hill PA 19000</p>
</main>
</body>
</html>
```